Bref créative |
Jewelry and Home ware website | ||
Studio Kelvara | ||
Jewelry | ||
www.studiokelvara.example | ||
Studio Kelvara is a new company which is just about to launch to the public. Studio Kelvara is a line of handmade jewelry and home ware made with semi precious materials. All pieces are designed and made by me (kela) Rosalind Theda Quarrington. At the moment the brand is very small and the website will be primary used as an online catalogue, eventually hoping to start online buying. | ||
Clean and simple designs, nothing to distract from pieces. |
Clean/Simple Conservative Elegant Traditional Feminine |
Browns | ||
Beiges /Off Whites | ||
Natural tones | ||
left side | ||
View logo on company url. | ||

```html
<!DOCTYPE html>
<html lang="en">
<head>
<meta charset="utf-8">
<title>Studio Kelvara — Jewelry &amp; Home ware</title>
<link href="https://fonts.googleapis.com/css2?family=Lobster+Two:ital,wght@1,700&family=Arimo:wght@400;700&display=swap" rel="stylesheet">
<style>
  :root{
    --bg-brown:#3b2019;
    --nav-brown:#2e1a15;
    --ribbon:#3a221c;
    --ribbon-fold:#1e110d;
    --page:#ffffff;
    --frame:#d8d2c2;
    --panel:#e4e4e6;
    --thumb:#eeeeef;
    --ink:#2b1a15;
    --body-ink:#555555;
    --muted:#888888;
    --wood:#5b2f22;
    --silver:#c9c9cc;
  }
  *{box-sizing:border-box;margin:0;padding:0}
  html,body{width:1200px;height:1047px;overflow:hidden}
  body{background:var(--bg-brown);font-family:"Arimo",Arial,sans-serif;color:var(--body-ink);position:relative}
  .page{position:absolute;left:170px;top:0;width:860px;height:1047px;background:var(--page)}
  .brand{position:absolute;left:0;top:30px;width:1200px;display:flex;justify-content:center;align-items:center;gap:12px}
  .brand-dot{width:16px;height:16px;border-radius:50%;background:var(--ink)}
  .brand-name{font-family:"Lobster Two",cursive;font-style:italic;font-weight:700;font-size:40px;color:var(--ink)}
  .main-nav{position:absolute;left:156px;top:134px;width:888px;height:38px;background:var(--nav-brown);border:2px solid #d9d9d9;outline:1px solid #555;display:flex;align-items:center}
  .main-nav a{flex:1;text-align:center;color:#fff;font-size:16px;text-decoration:none}
  .main-nav a.active{text-decoration:underline}
  .slider{position:absolute;left:184px;top:184px;width:832px;height:417px;background:var(--frame);padding:20px}
  .slide-main{width:792px;height:307px;
    background:
      radial-gradient(ellipse 38% 30% at 30% 50%, rgba(91,47,34,.85), rgba(91,47,34,0) 70%),
      radial-gradient(ellipse 38% 30% at 72% 45%, rgba(91,47,34,.8), rgba(91,47,34,0) 70%),
      radial-gradient(ellipse 30% 35% at 50% 65%, rgba(255,255,255,.9), rgba(255,255,255,0) 70%),
      linear-gradient(180deg,#e6e6e8,#c9c9cc);}
  .thumbs{display:flex;gap:10px;margin-top:12px}
  .thumb{width:150px;height:66px;border:2px solid #fff}
  .thumb.t1{background:radial-gradient(ellipse at 40% 50%,#3f7f8c,#c9cbcf 55%,#eeeeef)}
  .thumb.t2{background:radial-gradient(ellipse at 55% 50%,#6a3a2a,#cfcfd2 55%,#eeeeef)}
  .thumb.t3{background:radial-gradient(ellipse at 50% 50%,#b8b8bc,#eeeeef 65%)}
  .thumb.t4{background:radial-gradient(ellipse at 50% 50%,#5b2f22,#bcb6b3 55%,#e2e2e4)}
  .thumb.t5{background:radial-gradient(ellipse at 50% 50%,#c9a24a,#d9d9dc 55%,#f4f4f5)}
  .thumb.current{border-color:#6b6b6b}
  .features{position:absolute;left:193px;top:630px;display:flex;gap:28px}
  .feature{position:relative;width:250px;height:170px}
  .feature-img{width:250px;height:148px}
  .feature-img.f1{background:radial-gradient(ellipse 40% 40% at 50% 45%,#4d8a98,#c4c6ca 60%,#e4e4e6)}
  .feature-img.f2{background:radial-gradient(ellipse 35% 42% at 50% 45%,#5b2f22,#b3a7a2 60%,#e4e4e6)}
  .feature-img.f3{background:radial-gradient(ellipse 40% 40% at 50% 45%,#6a3a2a,#c8c5c5 60%,#e4e4e6)}
  .ribbon{position:absolute;left:-6px;top:126px;width:262px;height:38px;background:var(--ribbon);color:#fff;font-family:"Lobster Two",cursive;font-style:italic;font-weight:700;font-size:21px;line-height:38px;padding:0 22px 0 14px;
    clip-path:polygon(0 0,100% 0,96% 50%,100% 100%,0 100%)}
  .fold{position:absolute;left:-6px;top:164px;width:0;height:0;border-top:6px solid var(--ribbon-fold);border-left:6px solid transparent}
  .about{position:absolute;left:193px;top:816px;width:530px}
  .section-title{font-family:"Lobster Two",cursive;font-style:italic;font-weight:700;font-size:23px;color:var(--ink);margin-bottom:8px;white-space:nowrap}
  .about p{font-size:11.5px;line-height:16px;color:var(--body-ink)}
  .read-more{display:block;margin-top:12px;font-size:12px;color:var(--ink);text-decoration:none}
  .newsletter{position:absolute;left:755px;top:816px;width:252px}
  .newsletter p{font-size:11.5px;line-height:16px}
  .signup{display:flex;gap:8px;margin-top:10px}
  .signup input{width:170px;height:26px;border:1px solid #bbb;font-size:10px;padding:0 6px;color:var(--muted);font-family:inherit}
  .signup button{width:72px;height:26px;background:var(--ribbon);color:#fff;border:0;font-size:13px;font-family:inherit}
  .social{display:flex;gap:10px;margin-top:16px}
  .social span{width:30px;height:30px;background:var(--ribbon);border-radius:3px}
  .footer{position:absolute;left:193px;top:992px;width:814px;border-top:1px solid #ddd;text-align:center;padding-top:8px;font-size:11.5px;color:var(--ink)}
  .footer nav a{color:var(--ink);text-decoration:none;margin:0 4px}
  .copyright{margin-top:6px;font-size:11px}
</style>
</head>
<body>
  <div class="page"></div>

  <header class="brand">
    <span class="brand-dot"></span>
    <span class="brand-name">Studio Kelvara</span>
  </header>

  <nav class="main-nav">
    <a href="#" class="active">Home</a>
    <a href="#">About Us</a>
    <a href="#">Jewelry</a>
    <a href="#">Home wmade</a>
    <a href="#">Contact Us</a>
  </nav>

  <section class="slider">
    <div class="slide-main" role="img" aria-label="Handmade silver spoons with carved dark wood handles arranged on a pale grey surface"></div>
    <div class="thumbs">
      <div class="thumb t1" role="img" aria-label="Silver ring with teal stone"></div>
      <div class="thumb t2" role="img" aria-label="Silver spoon with wooden handle"></div>
      <div class="thumb t3" role="img" aria-label="Silver bangle"></div>
      <div class="thumb t4 current" role="img" aria-label="Wood-handled spoons"></div>
      <div class="thumb t5" role="img" aria-label="Gold and silver earrings"></div>
    </div>
  </section>

  <section class="features">
    <article class="feature">
      <div class="feature-img f1" role="img" aria-label="Silver flower ring with blue stones"></div>
      <div class="ribbon">Jewelry</div><span class="fold"></span>
    </article>
    <article class="feature">
      <div class="feature-img f2" role="img" aria-label="Dark wooden napkin ring"></div>
      <div class="ribbon">Home Wmade</div><span class="fold"></span>
    </article>
    <article class="feature">
      <div class="feature-img f3" role="img" aria-label="Silver spoon with wooden handle"></div>
      <div class="ribbon">Latest Product</div><span class="fold"></span>
    </article>
  </section>

  <section class="about">
    <h2 class="section-title">Meet Rosalind Theda Quarrington (Kela)</h2>
    <p>Lorem ipsum dolor sit amet, consectetur adipiscing elit, sed do eiusmod tempor incididunt ut labore et dolore magna aliqua. Ut enim ad minim veniam, quis nostrud exercitation ullamco laboris nisi ut aliquip ex ea commodo consequat. Duis aute irure dolor in reprehenderit in voluptate velit esse cillum dolore eu fugiat nulla pariatur. Excepteur sint occaecat cupidatat non proident, sunt in culpa qui officia deserunt mollit anim id est laborum. Ut enim ad minim veniam, quis nostrud exercitation ullamco laboris nisi ut aliquip ex ea commodo consequat.</p>
    <a href="#" class="read-more">Read More...</a>
  </section>

  <aside class="newsletter">
    <h2 class="section-title">Newsletter</h2>
    <p>Join our list for news on new pieces, studio updates and launch dates delivered to your inbox.</p>
    <form class="signup">
      <input type="text" value="Enter Your Email">
      <button type="button">Signup</button>
    </form>
    <div class="social"><span></span><span></span></div>
  </aside>

  <footer class="footer">
    <nav><a href="#">Home</a>|<a href="#">About Us</a>|<a href="#">Jewelry</a>|<a href="#">Home wmade</a>|<a href="#">Contact Us</a></nav>
    <p class="copyright">Copyright 2013</p>
  </footer>
</body>
</html>
```